Verpackungsdesign für Pflanzentopf
Zielgruppe
Wir sind Hersteller von einem einzigartigen patentierten farbigen Pflanzensubstraten mit passendem Pflanzentopf, was zusammen ein einmaliges Pflanzensystem ergibt.
Unsere Zielgruppe sind Frauen, welche Orchideen als Zimmerpflanzen nutzen.
Aufgabenstellung
Unser Pflanzentopf soll in eine Umverpackung, welche gleichzeitig als Verkaufsverpackung dient.
Es soll eine Stanzkontur an der Verpackung enthalten sein, um den Pflanzentopf in der Verpackung sehen zu können.
Die Verpackung sollte Wertigkeit und die Genialität unseres Pflanzensystems mit seinem besonderen Nutzen vermitteln und ist gedacht für den Verkauf in Baumärkten, Gartenmärkten etc..
Unser Pflanzentopf ist 132x132 mm und 131 mm hoch
Vorteile unseres Pflanzentopfes mit unserm Orchideensubstrat zusammen im Überblick:
- versorgt die Pflanze mit Nährstoffen, kein Düngen notwendig
- hemmt Schimmel, es wächst kein Schimmel auf oder in unserem Substrat, deshalb auch für Allergiker eine Alternative
- hemmt Ungeziefer, Trauermücken, Wollläuse etc. niesten sich in unserem Boden nicht ein
- sorgt für ideale Substrat-Belüftung
- vereinfacht die Pflege von Orchideen
- vereinfacht das Gießen
- kein üblicher Schmutz wie bei anderen Pflanzenerden, bleibt sauber und zersetzt sich nicht
- das Reinigen des Topfes ist einfach, geschieht schnell und ohne den üblichen Schmutz
- ist nachhaltig, unser Substrat arbeitet als Ionenaustauscher und ist mindesten 5-8 Jahre aktiv und auch später muss nichts weggeworfen werden, weil es dann immer noch schön aussieht und trotzdem weiterverwendet werden kann

```html
<!DOCTYPE html>
<html lang="de">
<head>
<meta charset="utf-8">
<title>Varunel – Verpackung Rückseite</title>
<link href="https://fonts.googleapis.com/css2?family=Montserrat:wght@800&family=Outfit:wght@300;400;600;700&display=swap" rel="stylesheet">
<style>
  :root {
    --kraft-light: #c59c6d;
    --kraft-mid: #b48a5d;
    --kraft-dark: #a4784f;
    --brand-red: #d10000;
    --ink: #1f1f1f;
    --white: #ffffff;
  }
  * { margin: 0; padding: 0; box-sizing: border-box; }
  html, body { width: 1200px; height: 1200px; overflow: hidden; }
  body { background: #f4f4f4; }

  .package-back {
    position: relative;
    width: 1200px;
    height: 1200px;
    overflow: hidden;
    background: linear-gradient(160deg, var(--kraft-light) 0%, var(--kraft-mid) 55%, var(--kraft-dark) 100%);
    font-family: "Outfit", sans-serif;
    color: var(--ink);
  }

  .kraft-texture {
    position: absolute;
    inset: 0;
    width: 1200px;
    height: 1200px;
    mix-blend-mode: multiply;
    opacity: 0.35;
    pointer-events: none;
  }

  .headline-pill {
    position: absolute;
    height: 81px;
    border-radius: 40px;
    background: var(--brand-red);
    color: var(--white);
    font-family: "Montserrat", sans-serif;
    font-weight: 800;
    font-size: 34px;
    line-height: 81px;
    white-space: nowrap;
  }
  .headline-pill--first { left: 55px; top: 100px; width: 768px; padding-left: 21px; }
  .headline-pill--second { left: 230px; top: 171px; width: 688px; padding-left: 31px; }

  .body-copy {
    position: absolute;
    left: 101px;
    top: 300px;
    width: 900px;
    font-weight: 700;
    font-size: 25px;
    letter-spacing: 1.7px;
    line-height: 30.7px;
    white-space: nowrap;
  }
  .body-copy p + p { margin-top: 30.7px; }

  .tagline {
    position: absolute;
    left: 522px;
    top: 716px;
    white-space: nowrap;
    font-weight: 600;
    font-size: 42px;
    letter-spacing: 0.8px;
    line-height: 64px;
  }
  .tagline strong { font-size: 51px; font-weight: 600; }
  .tagline-rule {
    position: absolute;
    left: 519px;
    top: 790px;
    width: 238px;
    height: 7px;
    border-radius: 4px;
    background: var(--brand-red);
  }

  .brand-name {
    position: absolute;
    left: 328px;
    top: 912px;
    font-weight: 400;
    font-size: 78px;
    line-height: 80px;
    color: var(--brand-red);
    letter-spacing: 1px;
  }

  .manufacturer {
    position: absolute;
    left: 335px;
    top: 998px;
    font-style: normal;
    font-weight: 300;
    font-size: 24px;
    letter-spacing: 0.8px;
    line-height: 28.6px;
  }

  .orchid-illustration {
    position: absolute;
    left: 868px;
    top: 801px;
    width: 240px;
    height: 399px;
  }
</style>
</head>
<body>
  <main class="package-back">
    <svg class="kraft-texture" viewBox="0 0 1200 1200" aria-hidden="true">
      <filter id="kraftGrain">
        <feTurbulence type="fractalNoise" baseFrequency="0.012 0.02" numOctaves="4" seed="7" result="mottle"/>
        <feColorMatrix in="mottle" type="matrix" values="0 0 0 0 0.55  0 0 0 0 0.38  0 0 0 0 0.22  0 0 0 1.4 -0.45"/>
      </filter>
      <filter id="kraftFibre">
        <feTurbulence type="fractalNoise" baseFrequency="0.9" numOctaves="2" seed="3"/>
        <feColorMatrix type="matrix" values="0 0 0 0 0.4  0 0 0 0 0.28  0 0 0 0 0.16  0 0 0 0.9 -0.35"/>
      </filter>
      <rect width="1200" height="1200" filter="url(#kraftGrain)"/>
      <rect width="1200" height="1200" filter="url(#kraftFibre)"/>
    </svg>

    <div class="headline-pill headline-pill--first">DEIN FARBIGES PFLANZENSUBSTRAT</div>
    <div class="headline-pill headline-pill--second">MIT PASSENDEN PFLANZENTOPF</div>

    <div class="body-copy">
      <p>Lorem ipsum dolor sit amet, consectetuer adipiscing elit, sed<br>diam nonummy nibh euismod tincidunt ut laoreet dolore magna<br>aliquam erat volutpat. Ut wisi enim ad minim veniam, quis<br>nostrud exerci tation ullamcorper suscipit lobortis nisl ut<br>aliquip ex ea commodo consequat.</p>
      <p>aliquam erat volutpat. Ut wisi enim ad minim veniam, quis<br>nostrud exerci tation ullamcorper suscipit lobortis nisl ut<br>aliquip ex ea commodo consequat.</p>
    </div>

    <div class="tagline">für deine <strong>Orchideen</strong></div>
    <div class="tagline-rule"></div>

    <div class="brand-name">Varunel</div>
    <address class="manufacturer">
      Hergestellt in:<br>
      Unternehmernamen<br>
      Adressenstr. 30<br>
      12556 Stadtname
    </address>

    <svg class="orchid-illustration" viewBox="0 0 240 399" role="img" aria-label="Strichzeichnung zweier Orchideenblüten im Pflanzentopf">
      <defs>
        <linearGradient id="orchidArea" x1="0" y1="0" x2="0" y2="1">
          <stop offset="0" stop-color="#1f1f1f" stop-opacity="0.16"/>
          <stop offset="1" stop-color="#1f1f1f" stop-opacity="0.26"/>
        </linearGradient>
      </defs>
      <rect width="240" height="399" rx="8" fill="url(#orchidArea)"/>
    </svg>
  </main>
</body>
</html>
```